Mental Health Therapy Website

I need a design for a mental health therapy website. It is a private practice. The business name is Brindle Counseling, PLLC. My name is Martin Hale, LMHC, NCC, DCC. I would like some of the features/menus to be Home; Welcome/About Me, Rates and Services, Common Questions, and Contact.
If possible I would like a blog on the main page that I can update with articles I write. I would like the contact page to feature a map to my location (4318 Cedarbend Ave. E, Lakewood, WA 98499).
I would like to place a small photo of me on the Welcome/About page.
I am new to this so if I am forgetting anything, please ask me!!
I will upload my logo so you can fit it and the color scheme into the design.
Thank you so very much!

```html
<!DOCTYPE html>
<html lang="en">
<head>
<meta charset="utf-8">
<title>Brindle Counseling</title>
<link href="https://fonts.googleapis.com/css2?family=Droid+Sans:wght@400;700&family=Droid+Serif:wght@400;700&display=swap" rel="stylesheet">
<style>
  :root {
    --blue: #34639b;
    --blue-nav: #3f6c9f;
    --green: #6c9f37;
    --text: #666a6e;
    --muted: #9a9a9a;
    --panel: #f0f0f0;
    --header-top: #ffffff;
    --header-bottom: #e4ebf4;
    --white: #ffffff;
  }
  * { margin: 0; padding: 0; box-sizing: border-box; }
  html, body { width: 1200px; height: 820px; overflow: hidden; }
  body {
    background: var(--white);
    font-family: "Droid Sans", "Noto Sans", sans-serif;
    color: var(--text);
  }
  .site-header {
    height: 109px;
    background: linear-gradient(to bottom, var(--header-top), var(--header-bottom));
  }
  .wrap { width: 982px; margin: 0 auto; position: relative; }
  .site-header .wrap { display: flex; align-items: center; justify-content: space-between; height: 109px; }
  .brand { display: flex; align-items: center; gap: 10px; }
  .brand-mark { width: 30px; height: 30px; border-radius: 50%; background: var(--blue); }
  .brand-name {
    font-family: "Droid Serif", serif;
    font-weight: 700;
    font-size: 26px;
    color: var(--blue);
  }
  .main-nav { display: flex; gap: 0; }
  .main-nav a {
    font-family: "Droid Serif", serif;
    font-weight: 700;
    font-size: 16px;
    color: var(--green);
    text-decoration: none;
    padding: 11px 12px;
    margin-left: 10px;
  }
  .main-nav a.is-active { background: var(--blue-nav); color: var(--white); }
  .content { display: flex; justify-content: space-between; padding-top: 35px; }
  .posts { width: 600px; }
  .post { margin-bottom: 14px; }
  .post-title {
    font-family: "Droid Serif", serif;
    font-weight: 700;
    font-size: 27px;
    color: var(--blue);
    margin-bottom: 8px;
  }
  .post-date { font-size: 15px; color: var(--muted); margin-bottom: 6px; }
  .post p { font-size: 15px; line-height: 23px; margin-bottom: 22px; }
  .post-comments { font-weight: 700; font-size: 15px; color: var(--green); text-decoration: none; }
  .sidebar { width: 338px; }
  .about-box { background: var(--panel); padding: 16px 14px 20px; }
  .about-box h3 {
    font-family: "Droid Serif", serif;
    font-weight: 700;
    font-size: 15.5px;
    color: var(--green);
    margin-bottom: 10px;
  }
  .about-photo {
    display: block;
    width: 292px; height: 229px;
    margin: 0 auto 12px;
    border: 1px solid #b5b5b5;
    background: linear-gradient(135deg, #e7ecf4 0%, #c9ccd3 45%, #e3e7ef 100%);
  }
  .about-box p { font-size: 12px; line-height: 20.5px; }
  .side-heading {
    font-family: "Droid Serif", serif;
    font-weight: 700;
    font-size: 21px;
    color: var(--green);
    margin: 22px 0 6px;
  }
  .latest li { list-style: none; }
  .latest a {
    font-family: "Droid Serif", serif;
    font-size: 18px;
    line-height: 30.5px;
    color: var(--blue);
    text-decoration: none;
  }
  .social { display: flex; gap: 10px; margin-top: 10px; }
  .social span { width: 35px; height: 35px; border-radius: 5px; background: var(--blue); display: block; }
</style>
</head>
<body>
  <header class="site-header">
    <div class="wrap">
      <div class="brand">
        <span class="brand-mark"></span>
        <span class="brand-name">Brindle Counseling</span>
      </div>
      <nav class="main-nav">
        <a href="#" class="is-active">Home</a>
        <a href="#">About Me</a>
        <a href="#">Rates and Services</a>
        <a href="#">Common Questions</a>
        <a href="#">Contact</a>
      </nav>
    </div>
  </header>

  <div class="wrap content">
    <main class="posts">
      <article class="post">
        <h2 class="post-title">This is a blog post title</h2>
        <div class="post-date">22nd January 2014</div>
        <p>Lorem ipsum dolor sit amet, eius debitis scribentur ne vix, eu error deseruisse sed, dicat interesset in eam. Sea vide aliquando id. Vocent audire viderer mei at, sea at mucius labore dignissim. Mea virtute liberavisse et, at usu adhuc dolores qualisque. In qui tollit epicurei sadipscing, timeam prompta eligendi qui ea, ea duo harum pertinax. Cibo laboramus vix at.</p>
        <p>Ei vitae sanctus necessitatibus per. Omnis essent vivendum mel ne, ad nemore doctus integre usu. Per cu audire definitionem, ei facer vituperatoribus cum, eam in graeco maluisset. Has explicari urbanitas democritum no, sed sale mazim praesent eu, mundi alterum te sed.</p>
        <p>Est no diam agam sadipscing. Eum solet moderatius te, pri blandit ullamcorper ea. Dicat tempor debitis ne duo, ei nam recusabo argumentum. Ad qui laudem viderer discere. Semper facete accusata sit eu</p>
        <a href="#" class="post-comments">3 comments</a>
      </article>
      <article class="post">
        <h2 class="post-title">And another blog post title</h2>
        <div class="post-date">22nd January 2014</div>
        <p>Lorem ipsum dolor sit amet, eius debitis scribentur ne vix, eu error deseruisse sed, dicat interesset in eam. Sea vide aliquando id. Vocent audire viderer mei at, sea at mucius labore dignissim. Mea virtute liberavisse et, at usu adhuc dolores qualisque. In qui tollit epicurei sadipscing, timeam prompta eligendi qui ea, ea duo harum pertinax. Cibo laboramus vix at.</p>
        <p>Ei vitae sanctus necessitatibus per. Omnis essent vivendum mel ne, ad nemore doctus integre usu.</p>
      </article>
    </main>

    <aside class="sidebar">
      <section class="about-box">
        <h3>My name is Martin Hale, LMHC, NCC, DCC.</h3>
        <div class="about-photo" role="img" aria-label="Portrait photo of the therapist"></div>
        <p>Est no diam agam sadipscing. Eum solet moderatius te, pri blandit ullamcorper ea. Dicat tempor debitis ne duo, ei nam recusabo argumentum. Ad qui laudem viderer discere. Semper facete accusata sit eu</p>
      </section>
      <h3 class="side-heading">Latest Posts</h3>
      <ul class="latest">
        <li><a href="#">This is a blog post title</a></li>
        <li><a href="#">And another blog post title</a></li>
        <li><a href="#">Benefits on meditation</a></li>
        <li><a href="#">Symptoms of Depression</a></li>
        <li><a href="#">Yet another blog post depresssion</a></li>
      </ul>
      <h3 class="side-heading">Follow me on Social Media</h3>
      <div class="social">
        <span aria-label="Social link 1"></span>
        <span aria-label="Social link 2"></span>
        <span aria-label="Social link 3"></span>
        <span aria-label="Social link 4"></span>
      </div>
    </aside>
  </div>
</body>
</html>
```